Design of a can of the adaptogenic drink brand "Brivana" (vector)

Please take the cans from the brief and make a print-ready vector with the instructions as in the other photos.

Target Market(s)

Young, upper-middle class athlete

Industry/Entity Type

Agroalimentaire

Colors

Designer to choose colors to be used in the design.

Requirements
Must have
• Adaptogenic flawed water
Nice to have
• Sleek, classy and healthy

```html
<!DOCTYPE html>
<html lang="fr">
<head>
<meta charset="UTF-8">
<title>Brivana — Eau Adaptogène</title>
<link href="https://fonts.googleapis.com/css2?family=Arimo:wght@400;700&display=swap" rel="stylesheet">
<style>
  :root {
    --backdrop: #a39f9e;
    --label-base: #0c0c0d;
    --label-sheen: #161617;
    --label-band: #272727;
    --ink-violet: #6c6598;
    --ink-violet-soft: #5f5988;
  }
  html, body {
    margin: 0;
    padding: 0;
    width: 1200px;
    height: 1200px;
    overflow: hidden;
    background: var(--backdrop);
  }
  .canvas {
    position: relative;
    width: 1200px;
    height: 1200px;
  }
  .can-label {
    position: absolute;
    left: 443px;
    top: 236px;
    width: 314px;
    height: 754px;
    overflow: hidden;
    background: var(--label-base);
  }
  .label-swoosh {
    position: absolute;
    inset: 0;
    width: 100%;
    height: 100%;
  }
  .label-text {
    position: absolute;
    left: 0;
    width: 100%;
    text-align: center;
    font-family: "Arimo", Arial, sans-serif;
    color: var(--ink-violet);
    margin: 0;
    white-space: nowrap;
  }
  .brand-name {
    top: 280px;
    font-size: 62px;
    font-weight: 400;
    letter-spacing: 1px;
    line-height: 1;
  }
  .product-type {
    top: 488px;
    font-size: 20px;
    font-weight: 700;
    padding-left: 14px;
    box-sizing: border-box;
  }
  .brand-line {
    top: 525px;
    font-size: 16px;
    font-weight: 400;
    color: var(--ink-violet-soft);
    padding-left: 14px;
    box-sizing: border-box;
  }
  .volume {
    top: 632px;
    font-size: 18px;
    font-weight: 400;
    color: var(--ink-violet-soft);
  }
</style>
</head>
<body>
  <main class="canvas">
    <section class="can-label">
      <svg class="label-swoosh" viewBox="0 0 314 754" preserveAspectRatio="none" aria-hidden="true">
        <path d="M0 0 H200 C120 60 50 140 0 220 Z" fill="var(--label-sheen)"/>
        <path d="M0 354 C60 520 180 660 314 720 V754 H0 Z" fill="var(--label-band)"/>
      </svg>
      <h1 class="label-text brand-name">Brivana</h1>
      <p class="label-text product-type">Eau Adaptogène Aromatisée</p>
      <p class="label-text brand-line">Marque : Brivana</p>
      <p class="label-text volume">12 fl oz (355ml)</p>
    </section>
  </main>
</body>
</html>
```